Kelvora Ledger Web Design Contest

We would like for you to design a website for www.kelvoraledger-example.com. Kelvora Ledger is a CPA Firm offering accounting, auditing, and tax preparation services.

We would like to have a consistent feel with the logo, business card, envelope, and stationary designs that were created by another designer on PlanHive. Examples of each are attached. We would like the website to have a clean/modern style.

The website should include the following:

1. A general "Welcome" landing page
2. A "About the Company" page
3. A "Services Offered" page
4. A "Contact Us" form
5. A button for "Sign up for Newsletter"

Target Market(s)

Individuals and businesses that require accounting, auditing, and tax preparation services from a CPA.

Industry/Entity Type

Accounting

Coding

Number of Pages Required

5+ page

Font styles to use
Other font styles liked:
• Trebuchet or similar

Requirements
Must have
• Consistent feel with logo and letterhead. The gray and blue bar on the letterhead should be incorporated into the website design.

```html
<!DOCTYPE html>
<html lang="en">
<head>
<meta charset="utf-8">
<title>Kelvora Ledger, LLC</title>
<link href="https://fonts.googleapis.com/css2?family=Open+Sans:wght@400;600;700&family=Raleway:wght@500;600&display=swap" rel="stylesheet">
<style>
:root{
  --navy:#00205f;
  --gray-dark:#555556;
  --gray-footer:#4c4c4c;
  --gray-band:#c3c3c3;
  --field:#ececec;
  --white:#ffffff;
}
*{margin:0;padding:0;box-sizing:border-box}
html,body{width:1200px;height:1110px;overflow:hidden}
body{position:relative;font-family:"Open Sans",sans-serif;color:var(--white);background:var(--white)}
.abs{position:absolute}

/* header */
.site-header{left:0;top:0;width:1200px;height:96px;background:var(--navy)}
.header-call{left:0;top:0;width:1200px;height:96px}
.brand{left:86px;top:14px;width:160px;text-align:center}
.brand-mark{display:block;width:36px;height:36px;border:2px solid var(--white);margin:0 auto 6px}
.brand-name{font-size:11px;font-weight:600;letter-spacing:.3px;white-space:nowrap}
.brand-tag{font-size:7px;letter-spacing:.6px;margin-top:2px;white-space:nowrap}
.main-nav{top:41px;left:416px;display:flex;font-size:12px;font-weight:600}
.main-nav a{color:var(--white);text-decoration:none;margin-right:50px}
.call{left:1022px;top:32px;display:flex;align-items:center;gap:14px}
.call-label{font-size:12px;color:#dcdcdc;line-height:14px}
.call-number{font-size:14px;font-weight:600}

/* hero */
.hero{left:0;top:96px;width:1200px;height:704px;border-top:3px solid var(--white);
  background:linear-gradient(100deg,#8a9aa6 0%,#6f7e8a 30%,#3d4651 55%,#5b5450 75%,#3a3634 100%)}
.hero-shade{left:0;top:96px;width:1200px;height:704px;background:linear-gradient(180deg,rgba(0,20,50,.05),rgba(0,20,50,.45))}
.arrow{width:42px;height:42px;border:2px solid var(--white);border-radius:50%}
.hero-square{left:517px;top:172px;width:166px;height:166px;border:7px solid var(--white)}
.hero-title{left:0;top:352px;width:1200px;text-align:center;font-size:50px;font-weight:600;letter-spacing:4px;white-space:nowrap}
.hero-tag{left:0;top:419px;width:1184px;text-align:center;font-family:"Raleway",sans-serif;font-weight:600;font-size:29px;letter-spacing:3.2px}
.feature-badge{left:117px;top:541px;width:188px;height:188px;border-radius:50%;background:var(--white);border:3px solid #d8d8d8}
.feature-title{left:354px;top:533px;font-size:35px;font-weight:600;letter-spacing:1px}
.feature-text{left:352px;top:587px;width:735px;font-size:14.6px;line-height:22.7px}
.read-more{left:350px;top:672px;width:124px;height:43px;background:var(--navy);border:1px solid var(--white);
  font-size:12px;font-weight:600;display:flex;align-items:center;justify-content:center;gap:10px}
.dot-nav{width:55px;height:55px;border-radius:50%;background:var(--navy);display:flex;align-items:center;justify-content:center}
.dot-nav.active{background:var(--white)}

/* newsletter */
.newsletter{left:0;top:800px;width:1200px;height:220px;background:var(--gray-band)}
.news-title{left:0;top:838px;width:1170px;text-align:center;font-family:"Raleway",sans-serif;font-weight:500;font-size:37px;color:var(--navy)}
.field{top:920px;height:51px;background:var(--field);color:#6a6a6a;font-size:12px;padding-left:15px;display:flex;align-items:center}
.sign-up{left:880px;top:919px;width:280px;height:52px;background:var(--navy);font-family:"Raleway",sans-serif;font-size:18px;display:flex;align-items:center;justify-content:center}

/* footer */
.site-footer{left:0;top:1020px;width:1200px;height:90px;background:var(--gray-footer)}
.footer-mark{left:56px;top:1046px;width:41px;height:41px;border:2px solid #9a9a9a}
.footer-links{left:0;top:1048px;width:1030px;text-align:center;font-size:12.5px}
.footer-links span{margin:0 4px}
.copyright{left:0;top:1075px;width:1030px;text-align:center;font-size:10px}
.social{top:1062px;width:12px;height:12px;border-radius:50%;background:#b9c2d6}
</style>
</head>
<body>

<header class="abs site-header"></header>
<svg class="abs header-call" viewBox="0 0 1200 96" aria-hidden="true"><polygon points="983,0 1200,0 1200,96 950,96" fill="var(--gray-dark)"/><polyline points="983,0 950,96" stroke="#ffffff" stroke-width="3" fill="none"/></svg>

<div class="abs brand">
  <span class="brand-mark"></span>
  <div class="brand-name">KELVORA LEDGER, LLC</div>
  <div class="brand-tag">Accounting · Audit · Tax Services</div>
</div>

<nav class="abs main-nav">
  <a href="#">HOME</a><a href="#">ABOUT THE COMPANY</a><a href="#">SERVICES OFFERED</a><a href="#">CONTACT US</a>
</nav>

<div class="abs call">
  <svg width="22" height="22" viewBox="0 0 24 24" aria-hidden="true"><path d="M6 3l3 4-2 2c1 2.5 3.5 5 6 6l2-2 4 3-2 3C10 19 5 14 3 6z" fill="#fff"/><path d="M14 3a7 7 0 0 1 7 7M14 6a4 4 0 0 1 4 4" stroke="#fff" stroke-width="1.6" fill="none"/></svg>
  <div><div class="call-label">CALL US</div><div class="call-number">555.010.4722</div></div>
</div>

<div class="abs hero" role="img" aria-label="Photo of hands with a pen reviewing financial charts beside a tablet"></div>
<div class="abs hero-shade"></div>

<div class="abs arrow" style="left:41px;top:314px"></div>
<svg class="abs" style="left:41px;top:314px" width="42" height="42" aria-hidden="true"><polyline points="24,14 17,21 24,28" stroke="#fff" stroke-width="2.4" fill="none"/></svg>
<div class="abs arrow" style="left:1104px;top:314px"></div>
<svg class="abs" style="left:1104px;top:314px" width="42" height="42" aria-hidden="true"><polyline points="18,14 25,21 18,28" stroke="#fff" stroke-width="2.4" fill="none"/></svg>

<div class="abs hero-square"></div>
<div class="abs hero-title">KELVORA LEDGER, LLC</div>
<div class="abs hero-tag">Accounting · Audit · Tax Services</div>

<div class="abs feature-badge"></div>
<svg class="abs" style="left:168px;top:594px" width="86" height="82" viewBox="0 0 86 82" aria-hidden="true">
  <path d="M22 4h58l-14 60H8z" fill="var(--navy)"/>
  <path d="M8 64h58l-2 8H8a5 5 0 0 1 0-8z" fill="#fff" stroke="var(--navy)" stroke-width="5"/>
  <rect x="28" y="16" width="34" height="6" fill="#fff"/><rect x="25" y="28" width="34" height="6" fill="#fff"/>
  <path d="M80 4l-14 60-2 8" stroke="var(--navy)" stroke-width="5" fill="none"/>
</svg>

<div class="abs feature-title">ACCOUNTING</div>
<p class="abs feature-text">Lorem ipsum dolor sit amet, consectetur adipiscing elit, sed do eiusmod tempor incididunt ut labore et dolore magna aliqua. Ut enim ad minim veniam, quis nostrud exercitation ullamco laboris nisi ut aliquip ex ea commodo consequat. Duis aute irure dolor in reprehenderit in voluptate velit esse&nbsp; pariatur.</p>
<div class="abs read-more">READ MORE <svg width="6" height="9" aria-hidden="true"><polygon points="0,0 6,4.5 0,9" fill="#fff"/></svg></div>

<div class="abs dot-nav active" style="left:914px;top:718px"><svg width="28" height="24" viewBox="0 0 86 82" aria-hidden="true"><path d="M22 4h58l-14 60H8z" fill="var(--navy)"/><path d="M8 64h58l-2 8H8a5 5 0 0 1 0-8z" fill="#fff" stroke="var(--navy)" stroke-width="6"/></svg></div>
<div class="abs dot-nav" style="left:985px;top:718px"><svg width="30" height="30" viewBox="0 0 30 30" aria-hidden="true"><path d="M10 3h11l5 5v18H10z" fill="none" stroke="#fff" stroke-width="2"/><line x1="16" y1="12" x2="22" y2="12" stroke="#fff" stroke-width="2"/><line x1="16" y1="17" x2="22" y2="17" stroke="#fff" stroke-width="2"/><circle cx="11" cy="17" r="5" fill="var(--navy)" stroke="#fff" stroke-width="2"/><line x1="7" y1="21" x2="3" y2="26" stroke="#fff" stroke-width="3"/></svg></div>
<div class="abs dot-nav" style="left:1051px;top:718px"><svg width="26" height="26" viewBox="0 0 26 26" aria-hidden="true"><rect x="2" y="5" width="22" height="19" fill="none" stroke="#fff" stroke-width="2"/><rect x="2" y="5" width="22" height="5" fill="#fff"/><line x1="8" y1="2" x2="8" y2="7" stroke="#fff" stroke-width="2"/><line x1="18" y1="2" x2="18" y2="7" stroke="#fff" stroke-width="2"/><text x="13" y="21" font-size="9" font-weight="700" text-anchor="middle" fill="#fff" font-family="Open Sans, sans-serif">15</text></svg></div>

<section class="abs newsletter"></section>
<h2 class="abs news-title">Join Our Newsletter!</h2>
<div class="abs field" style="left:56px;width:388px">Enter Your Name</div>
<div class="abs field" style="left:470px;width:388px">Enter Your Email Address</div>
<div class="abs sign-up">SIGN UP</div>

<footer class="abs site-footer"></footer>
<svg class="abs" style="left:0;top:1020px" width="1200" height="90" aria-hidden="true"><polygon points="950,0 1200,0 1200,90 920,90" fill="var(--navy)"/><polyline points="950,0 920,90" stroke="#fff" stroke-width="2" fill="none"/></svg>
<div class="abs footer-mark"></div>
<div class="abs footer-links">Home<span>/</span>About the Company<span>/</span>Services Offered<span>&nbsp;/&nbsp;</span>Contact Us</div>
<div class="abs copyright">© All Rights Reserved. Copyrights @Kelvora Ledger. 2015</div>
<div class="abs social" style="left:976px"></div>
<div class="abs social" style="left:1015px"></div>
<div class="abs social" style="left:1052px"></div>
<div class="abs social" style="left:1090px"></div>
<div class="abs social" style="left:1128px"></div>

</body>
</html>
```